VEMRA - new private security company in Guyana, South America needs a website & logo design

New private security company in Guyana needs a website ready for the company launch. The business will offer armed and unarmed security to high net worth individuals, politicians, government officials, diplomats and off-shore oil industry vessels and platforms.

The company has its own heliport and indoor training range, armoured vehicles, ambulances and uniformed security personnel, and we would like some imager to indicate this.

The team leaders are all ex-special forces.

The website structure should be something like:

PAGE 1 Home
PAGE 2 About Us
PAGE 3 Guyana Security Overview
PAGE 4 Services
PAGE 5 Contact Us
PAGE 6 Useful Links

We have uploaded a file with the text copy for each of these pages.

The web domain has been registered through Pellnet and is www.vemra.group

Target Market(s)

Corporations involved in the oil and gas industry, Embassies, Investment companies and individuals, Caribbean diaspora.

Industry/Entity Type

Security Service

Logo Text

VEMRA

Coding

Coded - Design and coding required

Number of Pages Required

5+ page

Font styles to use
Sans Serif

Requirements
Must have
• Must have:
an enquiry/contact form page
general location map: https://mapfold.example/loc/Kp82wQzLr5Ynb7Xh4;
text as per web content document uploaded to this site
Nice to have
• Images of private security (cars, bodyguards, helicopters/planes, etc)
Images of Maritime security (non-military)
Images of people of colour (Guyana has mainly afro and indian residents)
Image of a high tec security control room

```html
<!DOCTYPE html>
<html lang="en">
<head>
<meta charset="utf-8">
<title>VEMRA – Security Services Guyana</title>
<link rel="stylesheet" href="https://fonts.googleapis.com/css2?family=Montserrat:wght@500;600;700;800&family=Open+Sans:wght@400;600&display=swap">
<style>
:root{
  --red:#e3202e;
  --red-deep:#b8141f;
  --ink:#1d1e22;
  --panel:#25272c;
  --black:#0b0b0c;
  --white:#ffffff;
  --muted:#d7d7d9;
  --head:"Montserrat",sans-serif;
  --body:"Open Sans",sans-serif;
}
*{box-sizing:border-box;margin:0;padding:0}
html,body{width:685px;height:1200px;overflow:hidden;background:var(--ink)}
.page{position:relative;width:685px;height:1200px;overflow:hidden;font-family:var(--body);color:var(--white)}
.abs{position:absolute}

/* hero */
.hero{position:absolute;left:0;top:0;width:685px;height:352px;overflow:hidden}
.hero-photo{position:absolute;inset:0;background:linear-gradient(100deg,#3a3f47 0%,#2b2f35 35%,#4a4f57 60%,#23272d 100%)}
.hero-diagonal{position:absolute;inset:0}
.brand{position:absolute;left:99px;top:10px;width:46px;text-align:center}
.brand-dot{display:block;width:22px;height:22px;border-radius:50%;background:var(--red);margin:0 auto 4px}
.brand-name{font-family:var(--head);font-weight:600;font-size:12px;letter-spacing:.3px;color:var(--white)}
.nav{position:absolute;top:21px;left:216px;display:flex;gap:11px;font-family:var(--head);font-weight:600;font-size:5.6px;letter-spacing:.1px}
.nav a{color:var(--white);text-decoration:none;position:relative}
.nav a.active::after{content:"";position:absolute;left:0;right:0;bottom:-5px;height:1px;background:var(--white)}
.phone{position:absolute;left:501px;top:19px;font-family:var(--head);font-weight:500;font-size:8px;letter-spacing:.3px}
.btn{display:flex;align-items:center;justify-content:center;background:var(--red);color:var(--white);font-family:var(--head);font-weight:600;letter-spacing:.8px;border-radius:20px;box-shadow:0 0 0 1.5px rgba(227,32,46,.55)}
.btn-call{position:absolute;left:492px;top:38px;width:92px;height:18px;font-size:6.6px}
.hero-kicker{position:absolute;left:120px;top:131px;font-family:var(--head);font-weight:600;font-size:7.6px;letter-spacing:2.2px}
.hero-title{position:absolute;left:115px;top:136px;font-family:var(--head);font-weight:800;font-size:48px;letter-spacing:-.5px;line-height:1}
.hero-text{position:absolute;left:120px;top:190px;width:160px;font-size:5.8px;line-height:7.3px}
.btn-more{position:absolute;left:122px;top:236px;width:93px;height:19px;font-size:6px}
.slides{position:absolute;left:303px;top:297px;display:flex;align-items:center;font-family:var(--head);font-weight:500;font-size:6px}
.slides .bar{width:20px;height:1px;background:var(--red);margin:0 4px}
.slides span.n{margin-right:12px}
.badge{position:absolute;width:38px;height:38px;border-radius:50%;background:var(--white);box-shadow:0 1px 4px rgba(0,0,0,.4);display:flex;align-items:center;justify-content:center}
.badge::after{content:"";width:18px;height:18px;border-radius:50%;border:3px solid var(--red)}

/* services */
.services{position:absolute;left:0;top:352px;width:685px;height:275px;overflow:hidden}
.services-photo{position:absolute;inset:0;background:linear-gradient(120deg,#2c2f34 0%,#3b3f45 40%,#2a2d32 70%,#33363b 100%)}
.services-shade{position:absolute;inset:0;background:rgba(24,25,29,.45)}
.section-title{position:absolute;left:0;width:685px;text-align:center;font-family:var(--head);font-weight:800;font-size:21px;letter-spacing:.2px}
.services-intro{position:absolute;left:0;top:79px;width:685px;text-align:center;font-size:7.6px;line-height:10px}
.service{position:absolute;top:124px;width:120px;margin-left:-60px;text-align:center}
.service-ring{width:63px;height:63px;border-radius:50%;border:1px solid var(--white);margin:0 auto;display:flex;align-items:center;justify-content:center}
.service-ring.filled{background:var(--red);border-color:var(--red)}
.service-label{margin-top:15px;font-family:var(--head);font-weight:600;font-size:6.8px;letter-spacing:.9px;line-height:8.4px}
.arrow{position:absolute;top:144px}

/* about */
.about{position:absolute;left:0;top:627px;width:685px;height:259px;background:var(--panel)}
.about-title{position:absolute;left:99px;top:30px;font-family:var(--head);font-weight:800;font-size:21px}
.about-title em{font-style:normal;color:var(--red)}
.about-rule{position:absolute;left:99px;top:64px;width:37px;height:1.5px;background:var(--white)}
.about-col{position:absolute;top:82px;font-size:6.6px;line-height:9.65px;color:var(--muted)}
.about-col p{margin-bottom:9.3px}
.about-photo{position:absolute;left:445px;top:1px;width:232px;height:258px;background:linear-gradient(180deg,#3a3c42 0%,#1c1e24 55%,#15171c 100%);clip-path:polygon(18% 0,82% 0,100% 20%,100% 100%,0 100%,0 20%)}

/* contact */
.contact{position:absolute;left:0;top:886px;width:685px;height:177px;background:var(--red);overflow:hidden}
.contact-photo{position:absolute;left:380px;top:0;width:305px;height:177px;background:linear-gradient(90deg,rgba(150,10,20,0) 0%,rgba(140,12,22,.55) 40%,rgba(120,10,18,.35) 100%)}
.field{position:absolute;width:235px;height:27px;border:1px solid rgba(255,255,255,.85);font-family:var(--head);font-weight:600;font-size:7.4px;letter-spacing:1.6px;padding-left:7px;display:flex;align-items:center}
.btn-send{position:absolute;left:306px;top:135px;width:71px;height:18px;border-radius:10px;background:var(--black);color:var(--white);font-family:var(--head);font-weight:600;font-size:6.8px;letter-spacing:1px;display:flex;align-items:center;justify-content:center}

/* footer */
.footer{position:absolute;left:0;top:1063px;width:685px;height:137px;background:var(--black)}
.foot-head{position:absolute;top:17px;font-family:var(--head);font-weight:700;font-size:7px}
.foot-text{position:absolute;top:38px;font-family:var(--head);font-weight:500;font-size:5.6px;line-height:8px;color:var(--muted)}
.foot-links{position:absolute;top:38px;font-family:var(--head);font-weight:500;font-size:5.8px;line-height:11.3px;color:var(--muted)}
.social{position:absolute;top:35px;left:469px;display:flex;gap:3px}
.social span{width:14px;height:14px;border-radius:50%;background:#2c2d30}
.social span:first-child{background:var(--red)}
.foot-rule{position:absolute;left:0;top:106px;width:685px;height:1px;background:#2a2a2c}
.foot-bottom{position:absolute;top:117px;font-family:var(--head);font-weight:500;font-size:5.8px;color:var(--muted)}
.strip{position:absolute;left:0;bottom:0;width:685px;height:3px;background:#2b2c2f}
</style>
</head>
<body>
<div class="page">

  <header class="hero">
    <div class="hero-photo" role="img" aria-label="Photo of a bodyguard in a dark suit and sunglasses beside a car at night"></div>
    <svg class="hero-diagonal" width="685" height="352" viewBox="0 0 685 352">
      <polygon points="0,0 252,0 0,248" fill="#1f2024" opacity=".92"/>
      <polygon points="47,0 99,0 73,24" fill="var(--red)"/>
      <polygon points="580,274 656,352 502,352" fill="var(--red)"/>
    </svg>

    <div class="brand"><span class="brand-dot"></span><span class="brand-name">VEMRA</span></div>

    <nav class="nav">
      <a class="active" href="#">HOME</a>
      <a href="#">ABOUT US</a>
      <a href="#">GUYANA SECURITY OVERVIEW</a>
      <a href="#">SERVICES</a>
      <a href="#">CONTACT US</a>
    </nav>
    <div class="phone">+1(321) 555-01-47</div>
    <a class="btn btn-call">CALL US TODAY</a>

    <div class="hero-kicker">YOUR LIFE IS SAFE WITH</div>
    <h1 class="hero-title" style="top:139px">VEMRA</h1>
    <p class="hero-text">VEMRA is a fully licensed Guyanese security company offering a wide range of security services to the public and private sector and is a unique collaboration of highly trained Guyanese operatives...</p>
    <a class="btn btn-more">FIND OUT MORE</a>

    <div class="slides"><span>01</span><span class="bar"></span><span class="n">02</span><span class="n">03</span><span>04</span></div>
  </header>

  <section class="services">
    <div class="services-photo" role="img" aria-label="Photo of a security officer speaking into an earpiece beside a vehicle"></div>
    <div class="services-shade"></div>
    <h2 class="section-title" style="top:50px">OUR SERVICES</h2>
    <p class="services-intro">VEMRA offers the following services to protect you, your<br>colleagues, family, business or assets:</p>

    <svg class="arrow" style="left:89px" width="10" height="16" viewBox="0 0 10 16"><polyline points="8,1 2,8 8,15" fill="none" stroke="#fff" stroke-width="2"/></svg>
    <svg class="arrow" style="left:588px" width="10" height="16" viewBox="0 0 10 16"><polyline points="2,1 8,8 2,15" fill="none" stroke="#fff" stroke-width="2"/></svg>

    <div class="service" style="left:174px">
      <div class="service-ring">
        <svg width="28" height="28" viewBox="0 0 28 28" fill="none" stroke="#fff" stroke-width="1"><circle cx="14" cy="8" r="5"/><path d="M4 27v-5c0-4 4-7 10-7s10 3 10 7v5z"/><path d="M14 15l-2 12M14 15l2 12"/></svg>
      </div>
      <div class="service-label">UNARMED AND ARMED<br>CLOSE PROTECTION</div>
    </div>
    <div class="service" style="left:296px">
      <div class="service-ring filled">
        <svg width="26" height="28" viewBox="0 0 26 28" fill="none" stroke="#fff" stroke-width="1.2"><path d="M13 2l10 4v8c0 6-4 10-10 12C7 24 3 20 3 14V6z"/><path d="M13 6l6 2.5v5.5c0 4-2.5 6.5-6 8-3.5-1.5-6-4-6-8V8.5z"/><polyline points="9.5,14 12,16.5 16.5,11.5"/></svg>
      </div>
      <div class="service-label">STATIC &amp; MOBILE SECURITY<br>(ARMED AND UNARMED)</div>
    </div>
    <div class="service" style="left:412px">
      <div class="service-ring">
        <svg width="26" height="28" viewBox="0 0 26 28" fill="none" stroke="#fff" stroke-width="1.2"><circle cx="13" cy="10" r="5.5"/><path d="M6 10a7 7 0 0 1 14 0"/><path d="M4 26c0-5 4-8 9-8s9 3 9 8z"/><rect x="15" y="20" width="7" height="5"/></svg>
      </div>
      <div class="service-label">ADVANCED COVERT<br>SURVEILLANCE</div>
    </div>
    <div class="service" style="left:521px">
      <div class="service-ring">
        <svg width="28" height="28" viewBox="0 0 28 28" fill="none" stroke="#fff" stroke-width="1.1"><circle cx="14" cy="14" r="12"/><circle cx="14" cy="14" r="5"/><path d="M14 2v7M14 19v7M2 14h7M19 14h7"/></svg>
      </div>
      <div class="service-label">PERSONNEL AND<br>ASSET TRACKING</div>
    </div>
  </section>

  <div class="badge" style="left:323px;top:332px"></div>
  <div class="badge" style="left:323px;top:612px"></div>

  <section class="about">
    <div class="about-photo" role="img" aria-label="Photo of a security officer in a black suit and sunglasses holding a radio"></div>
    <h2 class="about-title">ABOUT <em>VEMRA</em></h2>
    <div class="about-rule"></div>
    <div class="about-col" style="left:99px;width:175px">
      <p>VEMRA is a fully licensed Guyanese security company offering a wide range of security services to the public and private sector and is a unique collaboration of highly trained Guyanese operatives and elite British military security experts.</p>
      <p>Our combination of local knowledge, contacts and resources teamed with years of active service in some of the most hostile regions in the world and high threat environments creates a highly capable, responsive and professional security service.</p>
      <p>We have years of experience of delivering effective security solutions to high net worth individuals and their families, multi-national corporations, royalty, politicians and valuable state owned and private assets.</p>
    </div>
    <div class="about-col" style="left:282px;width:158px">
      <p>We have developed the most advanced training offered to security personnel in Guyana, utilizing elite British operators and security doctrine and protocols developed over decades combined with a deep cultural understanding of the region.</p>
      <p>Our security operations are supported by the latest advanced technology and equipment and a wide-reaching intelligence network. Information, Technology, Training and Experience are the cornerstones of our operations.</p>
    </div>
  </section>

  <section class="contact">
    <div class="contact-photo" role="img" aria-label="Red-toned photo of a bodyguard standing beside a car"></div>
    <h2 class="section-title" style="top:20px">CONTACT US</h2>
    <div class="field" style="left:101px;top:57px">NAME</div>
    <div class="field" style="left:349px;top:57px">EMAIL</div>
    <div class="field" style="left:101px;top:94px">PHONE NUMBER</div>
    <div class="field" style="left:349px;top:94px">YOUR MESSAGE</div>
    <div class="btn-send">SEND</div>
  </section>

  <footer class="footer">
    <div class="foot-head" style="left:99px">About Us</div>
    <p class="foot-text" style="left:99px;width:112px">Lorem ipsum dolor sit amet, conse ctetur adipiscing elit, sed do eiusmod tempor incididunt ut labore et dolore magna aliqua.</p>

    <div class="foot-head" style="left:228px">Our Address</div>
    <p class="foot-text" style="left:228px;width:95px">Contact ba@vemra.group for further information or to arrange a security consultation.</p>

    <div class="foot-head" style="left:337px">Quick Links</div>
    <div class="foot-links" style="left:337px">About us<br>Our services<br>Contact us<br>Meet team</div>
    <div class="foot-links" style="left:397px">Privacy Policy<br>Testimonials<br>News<br>FAQ</div>

    <div class="foot-head" style="left:469px">Follow Us</div>
    <div class="social"><span></span><span></span><span></span></div>

    <div class="foot-rule"></div>
    <div class="foot-bottom" style="left:99px">Copyright © 2020 VEMRA . All Rights Reserved</div>
    <div class="foot-bottom" style="left:502px">Terms of Use &nbsp;| &nbsp;Privacy Policy</div>
    <div class="strip"></div>
  </footer>

</div>
</body>
</html>
```